TRADE SHOW DISPLAY BANNER Design Project

Looking for a designer to use some photos (that i have taken), edit, cut out, and design a banner for a trade show display that i will be using at an expo.

The approx visible size will be: 295cm wide x 230cm high
(please view display size 1 - for sizes, and display size 2 - for display end product)

Industry/Entity Type

Trade

Requirements
Must have
• - main focus is the steel fence post. will require a picture of the fence with the posts,
photos for this point are ( fence2, fence 3, fence 4, fence 5, fence1 original, fence1)

- the 3 pictures, outlining how the brackets work. on the side
photos for this point are (steel post 1, steel post 2, steel post 3)

Will require 'STEEL FENCE POST' written somewhere on top in large letters. will also require the website written somewhere on the add - 'www.BrindleRailWorks.com.au'

Will requite the orlevy timber logo somewhere on the bottom corners of the add.
photo of this add is - 'orlevy timber logo'

the exact dimensions of the add can be seen in 'display size1'
the end product of the add will look like 'display size2'

```html
<!DOCTYPE html>
<html lang="en">
<head>
<meta charset="utf-8">
<title>Steel Fence Post – Orlevy Timber</title>
<link href="https://fonts.googleapis.com/css2?family=Anton&family=Oswald:wght@700&display=swap" rel="stylesheet">
<style>
  :root {
    --navy: #0e3a6b;
    --navy-deep: #0a2d55;
    --sky-top: #5f9ad8;
    --sky-mid: #a9cbee;
    --sky-low: #e6eff8;
    --white: #ffffff;
    --bracket-grey: #b9b6ae;
    --bracket-wood: #cdbb94;
  }
  html, body {
    margin: 0;
    padding: 0;
    width: 1200px;
    height: 936px;
    overflow: hidden;
    background: var(--white);
  }
  .banner {
    position: relative;
    width: 1200px;
    height: 936px;
    overflow: hidden;
    background: var(--white);
    font-family: "Anton", "Oswald", sans-serif;
  }
  .hero-scene {
    position: absolute;
    inset: 0 0 160px 0;
    background:
      radial-gradient(ellipse 520px 320px at 260px 520px, rgba(222,190,140,.85), rgba(222,190,140,0) 70%),
      radial-gradient(ellipse 520px 200px at 900px 700px, rgba(110,170,60,.8), rgba(110,170,60,0) 70%),
      linear-gradient(180deg, var(--sky-top) 0%, var(--sky-mid) 35%, var(--sky-low) 70%, #f4f7fa 100%);
  }
  .headline {
    position: absolute;
    top: 40px;
    left: 0;
    width: 1200px;
    margin: 0;
    text-align: center;
    font-family: "Anton", sans-serif;
    font-weight: 400;
    font-size: 150px;
    line-height: 1;
    letter-spacing: 2px;
    color: var(--navy);
    text-shadow: 0 0 14px var(--white), 0 0 6px var(--white);
    transform: scaleY(1.05);
  }
  .features {
    position: absolute;
    top: 330px;
    left: 272px;
    margin: 0;
    padding: 0;
    list-style: none;
  }
  .features li {
    font-family: "Anton", sans-serif;
    font-size: 84px;
    line-height: 92px;
    color: var(--navy);
    letter-spacing: 1px;
    text-shadow: 0 0 10px var(--white), 0 0 4px var(--white);
  }
  .features li::before {
    content: "•";
    display: inline-block;
    width: 40px;
  }
  .callout-lines {
    position: absolute;
    left: 0;
    top: 0;
    width: 1200px;
    height: 760px;
  }
  .detail-card {
    position: absolute;
    left: 864px;
    top: 349px;
    width: 264px;
    height: 228px;
    box-sizing: border-box;
    border: 4px solid var(--navy);
    border-radius: 12px;
    overflow: hidden;
    background: var(--white);
  }
  .detail-photo {
    position: absolute;
    inset: 0 0 30px 0;
    background: linear-gradient(180deg, #f2f2f0 0%, var(--bracket-grey) 30%, var(--bracket-wood) 55%, var(--bracket-wood) 75%, #9a978f 100%);
  }
  .detail-label {
    position: absolute;
    left: 0;
    right: 0;
    bottom: 0;
    height: 30px;
    background: var(--navy);
    color: var(--white);
    font-family: "Oswald", sans-serif;
    font-weight: 700;
    font-size: 15px;
    line-height: 30px;
    text-align: center;
    letter-spacing: .3px;
  }
  .footer-band {
    position: absolute;
    left: 0;
    right: 0;
    bottom: 0;
    height: 172px;
    background: var(--white);
  }
  .footer-band::before {
    content: "";
    position: absolute;
    left: 0;
    right: 0;
    top: -20px;
    height: 20px;
    background:
      linear-gradient(-45deg, var(--white) 14px, transparent 0),
      linear-gradient(45deg, var(--white) 14px, transparent 0);
    background-size: 40px 20px;
    background-repeat: repeat-x;
    background-position: 0 100%;
  }
  .brand-row {
    position: absolute;
    left: 0;
    right: 0;
    top: 36px;
    display: flex;
    justify-content: space-around;
    align-items: center;
    padding: 0 40px;
  }
  .brand-name {
    display: flex;
    align-items: center;
    gap: 12px;
    font-family: "Anton", sans-serif;
    font-size: 46px;
    line-height: 1;
    color: var(--navy);
    letter-spacing: 1px;
    text-transform: uppercase;
  }
  .brand-mark {
    width: 22px;
    height: 22px;
    background: var(--navy);
  }
</style>
</head>
<body>
  <main class="banner">
    <div class="hero-scene" role="img" aria-label="Photo of a timber paling fence with slim steel posts on a green lawn under a blue sky"></div>

    <h1 class="headline">STEEL FENCE POST</h1>

    <ul class="features">
      <li>SLIM DESIGN</li>
      <li>LIGHTWEIGHT</li>
      <li>DURABLE</li>
    </ul>

    <svg class="callout-lines" viewBox="0 0 1200 760" aria-hidden="true">
      <circle cx="803" cy="447" r="28" fill="none" stroke="#0e3a6b" stroke-width="3"/>
      <line x1="822" y1="426" x2="868" y2="368" stroke="#0e3a6b" stroke-width="3"/>
      <line x1="822" y1="468" x2="868" y2="540" stroke="#0e3a6b" stroke-width="3"/>
    </svg>

    <figure class="detail-card" style="margin:0">
      <div class="detail-photo" role="img" aria-label="Close-up photo of a galvanised bracket fixing a timber rail to the steel post"></div>
      <figcaption class="detail-label">SECURE BRACKET SYSTEM</figcaption>
    </figure>

    <footer class="footer-band">
      <div class="brand-row">
        <div class="brand-name"><span class="brand-mark"></span>Orlevy Timber</div>
        <div class="brand-name"><span class="brand-mark"></span>Orlevy Timber</div>
        <div class="brand-name"><span class="brand-mark"></span>Orlevy Timber</div>
      </div>
    </footer>
  </main>
</body>
</html>
```